Business Card & Stationary Design for a PI Law Firm
Trial Attorneys Representing Injured Persons
I need double sided standard sized Business Card [3.5" x 2"]
use clean, modern fonts (ex: similar to a century gothic)
Bright & Fun-filled
Gregory T. Vasko
Vasko Legal Partners, LLC
418 N. Harlowe
Suite 0714
Chicago, IL 60417
vaskolegal@mailvo.net
www.vaskolegalpartners.net
Trial Attorneys Representing Injured Persons (Insert this tag line)
BUSINESS CARDS – double sided
The options are to do an assortment (up to 3) of the following:
1. front side in chocolate brown and back side in white (OR)
2. front side in the slate grey and back side in white
3. front side in lime green and back side in white
4. front side in orange and back side in white
STATIONARY:
The options are to utilize an assortment (up to 3) of the following options:
1. white background
2. white background with contrasting design elements in lime green
3. white background with contrasting design elements in orange
4. white background with contrasting design elements in chocolate brown
5. white background with contrasting design elements in slate grey
6. OR any combination of the above colors
ENVELOPES:
The options are to utilize an assortment (up to 3) of the following color options:
1. chocolate brown background
2. slate grey background
3. white background with contrast envelope fold color in slate grey
4. White background with contrast envelope fold chocolate brown
5. white background with contrast envelope fold in the lime green
6.. white background with contrast envelope fold in the orange
7. OR any combination of the above colors
WATERMARK-LIKE GRAPHICS in Stationary, Envelopes and Cards:
We would like to see a creative use of graphics for watermarks or shadows in the background of the business cards, stationery and envelopes. They can be colorful in lime green or orange or a combo of both or in chocolate brown and / or slate grey, but not too dark in saturation (as to be able to see any fonts).
LAYOUT for Cards and Stationary:
1. The layout should be clean and modern and utilize attractive and modern graphic symbols or mod bullet type points before each line of contact information.
2. Open to vertical layout or horizontal on business card.
3. Please include web address on envelope design perhaps in a separate area of the envelope from the return address.
White version

```html
<!DOCTYPE html>
<html lang="en">
<head>
<meta charset="utf-8">
<title>Vasko Legal Partners — Business Card</title>
<link rel="stylesheet" href="https://fonts.googleapis.com/css2?family=Questrial&display=swap">
<style>
  :root{
    --bg:#e9e8e6;
    --white:#ffffff;
    --orange:#f26a1b;
    --lime:#8cc63f;
    --brown:#4e2a12;
    --brown-soft:#5d3419;
    --ink:#3b2414;
  }
  *{margin:0;padding:0;box-sizing:border-box}
  html,body{width:1200px;height:998px;overflow:hidden;background:var(--bg)}
  body{font-family:"Questrial",sans-serif;position:relative}
  .card{position:absolute;top:345px;width:540px;height:309px;border-radius:18px;overflow:hidden;box-shadow:0 6px 18px rgba(0,0,0,.18)}
  .card--front{left:40px;background:var(--white)}
  .card--back{left:620px;background:var(--brown)}
  .front-shape{position:absolute;inset:0}
  .brand{position:absolute;left:34px;top:112px;display:flex;align-items:center;gap:10px}
  .brand__name{font-size:40px;color:var(--orange);letter-spacing:-.5px;line-height:1}
  .brand__dot{width:16px;height:16px;border-radius:50%;background:var(--lime)}
  .identity{position:absolute;left:300px;top:50px;color:var(--ink)}
  .identity__name{font-size:17px;font-weight:400}
  .identity__firm{font-size:12px;margin-top:3px}
  .contacts{position:absolute;left:300px;top:132px;list-style:none;color:var(--ink);font-size:11px;line-height:1}
  .contacts li{display:flex;align-items:center;gap:8px;height:19px}
  .contacts svg{width:13px;height:13px;flex:none}
  .back-web{position:absolute;left:24px;top:20px;font-size:13px;color:var(--orange);letter-spacing:1px}
  .back-mark{position:absolute;right:40px;bottom:70px;font-size:64px;color:var(--brown-soft);line-height:1}
</style>
</head>
<body>
  <section class="card card--front">
    <svg class="front-shape" viewBox="0 0 540 309" preserveAspectRatio="none">
      <path d="M258 309 C 236 210, 250 90, 330 0 L540 0 L540 309 Z" fill="var(--lime)"/>
      <path d="M272 309 C 252 210, 266 95, 346 0 L540 0 L540 309 Z" fill="var(--orange)"/>
    </svg>
    <div class="brand">
      <span class="brand__name">vasko</span>
      <span class="brand__dot"></span>
    </div>
    <div class="identity">
      <div class="identity__name">Gregory T. Vasko</div>
      <div class="identity__firm">Vasko Legal Partners, LLC</div>
    </div>
    <ul class="contacts">
      <li><svg viewBox="0 0 14 14"><circle cx="7" cy="7" r="7" fill="var(--brown)"/><path d="M7 3a2.5 2.5 0 0 0-2.5 2.5C4.5 8 7 11 7 11s2.5-3 2.5-5.5A2.5 2.5 0 0 0 7 3z" fill="#fff"/></svg>418 N. Harlowe, Suite 0714</li>
      <li><svg viewBox="0 0 14 14"><circle cx="7" cy="7" r="7" fill="var(--brown)"/></svg>Chicago, IL 60417</li>
      <li><svg viewBox="0 0 14 14"><circle cx="7" cy="7" r="7" fill="var(--brown)"/><path d="M4.5 3.5l1.5 0 .8 2-1 .8a5 5 0 0 0 1.9 1.9l.8-1 2 .8v1.5c0 .6-.5 1-1 1A6 6 0 0 1 3.5 4.5c0-.5.4-1 1-1z" fill="#fff"/></svg>312.555.0148</li>
      <li><svg viewBox="0 0 14 14"><circle cx="7" cy="7" r="7" fill="var(--brown)"/><rect x="4" y="4" width="6" height="6" fill="#fff"/></svg>312.555.0193</li>
      <li><svg viewBox="0 0 14 14"><circle cx="7" cy="7" r="7" fill="var(--brown)"/><rect x="3.5" y="4.5" width="7" height="5" fill="#fff"/></svg>vaskolegal@mailvo.net</li>
      <li><svg viewBox="0 0 14 14"><circle cx="7" cy="7" r="7" fill="var(--brown)"/><circle cx="7" cy="7" r="3.5" fill="none" stroke="#fff" stroke-width="1.2"/></svg>www.vaskolegalpartners.net</li>
    </ul>
  </section>

  <section class="card card--back">
    <div class="back-web">www.vaskolegalpartners.net</div>
    <div class="back-mark">vasko</div>
  </section>
</body>
</html>
```